Social Media Beitrag (Stelle)
Alles perfekt, sehr unkomplizierte Zusammenarbeit. Schnell ein passendes Design gefunden. Die Vorstellungen wurden super entgegengenommen und umgesetzt.
Zielgruppe
Wir sind eine allgemeinmedizinischen Tierklinik, welche Unterstützung im Team sucht. Aus diesem Grund ist die Zielgruppe bei dieser Arbeit potentielle Mitarbeiter.
Aufgabenstellung
Wir möchten gerne einen Social-Media-Beitrag beispielsweise auf Pixelbrunn und Kontaktwand machen und deshalb das Stelleninserat (im Anhang) in anderer verkürzter ansprechender Art darstellen. Ich stelle mir vor die Message auf ca. 3-4 quadratischen Bilder darzustellen, dass der Leser diese nacheinander ansehen kann und direkt angesprochen wird. Es muss nicht alles vom Stelleninserat mit eingebaut werden, sondern nur das wichtigste. Bei Pixelbrunn wäre ideale Größe für quadratische Posts ist 1080 px x 1080 px mit einem Seitenverhältnis von 1:1. Wir sind jedoch für andere Ideen offen oder wenn ihr auch das Gefühl habt wir packen die Message auf ein Bild. Ziel ist es möglichst ein breites Publikum online ansprechen zu können. Das Corporate Design der Unternehmung sollte auch mit berücksichtigt werden. Das Design sollte im Indesign oder Photoshop erstellt werden, damit wir es selbständig überarbeiten oder erweitern können.
Ich möchte keine BildVorrat-Personen auf den Post abbilden, dass wirkt zu künstlich, da es nicht die richtigen Mitarbeiter sind. Vielleicht kann auch etwas mit wenig Bild oder gar kein Bild und einfach einem Icon dargestellt werden.

```html
<!DOCTYPE html>
<html lang="de">
<head>
<meta charset="utf-8">
<title>Tierarzt sucht Helfer mit Herz und Verstand</title>
<link rel="stylesheet" href="https://fonts.googleapis.com/css2?family=Josefin+Sans:wght@400;600&family=Kaushan+Script&display=swap">
<style>
  :root {
    --panel-grey: #9c9d9f;
    --brand-red: #c8003c;
    --text-white: #ffffff;
    --heart-tone: #9a7f89;
    --photo-goldendoodle-a: #f3ece6;
    --photo-goldendoodle-b: #c0773f;
    --photo-cat-a: #5fb08c;
    --photo-cat-b: #e8e6e4;
    --photo-terrier-a: #f8e1d9;
    --photo-terrier-b: #3a2a24;
  }
  * { margin: 0; padding: 0; box-sizing: border-box; }
  html, body { width: 1200px; height: 1200px; overflow: hidden; }
  body { background: var(--panel-grey); }
  .post {
    position: relative;
    width: 1200px;
    height: 1200px;
    background: var(--panel-grey);
    overflow: hidden;
  }
  .photo-strip {
    position: absolute;
    top: 0; left: 0;
    width: 1200px;
    height: 458px;
    display: flex;
  }
  .photo {
    flex: 1 1 0;
    height: 100%;
  }
  .photo + .photo { margin-left: 1px; }
  .photo--doodle {
    background: radial-gradient(circle at 45% 50%, var(--photo-goldendoodle-b) 0%, #d59a66 45%, var(--photo-goldendoodle-a) 100%);
  }
  .photo--cat {
    background: radial-gradient(circle at 50% 55%, var(--photo-cat-b) 0%, #7a8f86 45%, var(--photo-cat-a) 80%);
  }
  .photo--terrier {
    background: radial-gradient(circle at 50% 45%, var(--photo-terrier-b) 0%, #8c6c5c 40%, var(--photo-terrier-a) 78%);
  }
  .heart-outline {
    position: absolute;
    left: 806px;
    top: 780px;
    width: 400px;
    height: 420px;
  }
  .eyebrow {
    position: absolute;
    left: 44px;
    top: 534px;
    font-family: "Josefin Sans", sans-serif;
    font-weight: 400;
    font-size: 64px;
    letter-spacing: 1px;
    color: var(--text-white);
    line-height: 1;
  }
  .headline {
    position: absolute;
    left: 36px;
    top: 620px;
    font-family: "Kaushan Script", cursive;
    font-weight: 400;
    color: var(--brand-red);
    font-size: 150px;
    line-height: 192px;
    letter-spacing: -2px;
    white-space: nowrap;
  }
  .headline span { display: block; }
  .job-title {
    position: absolute;
    left: 42px;
    top: 1036px;
    font-family: "Josefin Sans", sans-serif;
    font-weight: 400;
    font-size: 47px;
    letter-spacing: 2px;
    color: var(--text-white);
    line-height: 1;
    white-space: nowrap;
  }
</style>
</head>
<body>
  <main class="post">
    <div class="photo-strip">
      <div class="photo photo--doodle" role="img" aria-label="Foto: rotbrauner Goldendoodle mit heraushängender Zunge vor hellem Hintergrund"></div>
      <div class="photo photo--cat" role="img" aria-label="Foto: schwarz-weisse Katze mit grünen Augen vor grünem Hintergrund"></div>
      <div class="photo photo--terrier" role="img" aria-label="Foto: dreifarbiger Jack Russell Terrier vor zartrosa Hintergrund"></div>
    </div>

    <svg class="heart-outline" viewBox="0 0 400 420" aria-hidden="true">
      <path d="M200 118 C160 40 60 20 30 100 C5 170 60 250 200 400 C340 250 395 170 370 100 C340 20 240 40 200 118 Z"
            fill="none" stroke="var(--heart-tone)" stroke-width="17" stroke-linejoin="round"/>
    </svg>

    <p class="eyebrow">TIERARZT</p>
    <h1 class="headline">
      <span>Sucht Helfer mit</span>
      <span>Herz und Verstand</span>
    </h1>
    <p class="job-title">MITARBEITER/IN EMPFANG TPA (80-100%)</p>
  </main>
</body>
</html>
```